Orthopedic Arm Surgeon Brochure

Bifold modern design. I will supply the text, my photo, and photos of my textbooks. Prefer colors in the greens, blues, greys. For more information visit LimbForwardClinic.com Please feel free to e-mail me with any questions. Current brochure attached; I want to modernize this, get rid of frames, and change the text.

Target Market(s)

High-end market

Colors
3176b5
33a6d7
33b8a4
abd036
876aae
b768aa

Requirements
Must have
• Beautiful finishes
Should not have
• Bright reds, yellows, oranges that emit fear

```html
<!DOCTYPE html>
<html lang="en">
<head>
<meta charset="utf-8">
<title>Northridge Orthopedic Group – Bifold Brochure</title>
<link href="https://fonts.googleapis.com/css2?family=Lato:ital,wght@0,400;0,700;0,900;1,400&display=swap" rel="stylesheet">
<style>
:root{
  --bg:#4b4b4b;
  --paper:#ffffff;
  --green:#1e6a31;
  --green-dark:#15521f;
  --grey-text:#4a4a4a;
  --grey-soft:#e6e6e6;
  --grey-mid:#bdbdbd;
  --accent:#d9a441;
}
*{margin:0;padding:0;box-sizing:border-box}
html,body{width:1200px;height:1200px;overflow:hidden}
body{background:var(--bg);font-family:"Lato",sans-serif;color:var(--grey-text);position:relative}
.spread{position:absolute;left:200px;width:800px;height:540px;display:flex;box-shadow:0 10px 30px rgba(0,0,0,.45)}
.spread--outside{top:30px}
.spread--inside{top:630px}
.page{position:relative;width:400px;height:540px;background:var(--paper);overflow:hidden}
.page--left{background:linear-gradient(90deg,#fff 85%,#ececec 100%)}
.page--right{background:linear-gradient(90deg,#e9e9e9 0%,#fff 15%)}
.band{position:absolute;left:0;bottom:0;width:400px;height:140px;z-index:1}
.brand{position:absolute;z-index:2;font-family:"Lato",sans-serif;font-weight:700;color:var(--green);line-height:1.05;display:flex;align-items:center;gap:8px}
.brand__dot{width:12px;height:12px;border-radius:50%;background:currentColor;flex:none}
.brand__name{font-size:18px;letter-spacing:.5px}
.brand__sub{display:block;font-size:11px;letter-spacing:.2px}
.brand--light{color:#fff}
.web{position:absolute;z-index:2;color:#fff;font-size:9px;letter-spacing:3px}
.placeholder{position:absolute}
.books{left:55px;top:22px;width:300px;height:60px;background:linear-gradient(90deg,#b9862e,#b3262f 25%,#2b4f8a 45%,#7a3b23 65%,#5b2b6e 80%,#a3233a);opacity:.9}
.books-fade{position:absolute;left:55px;top:82px;width:300px;height:20px;background:linear-gradient(180deg,rgba(180,180,180,.35),rgba(255,255,255,0))}
.portrait{left:38px;top:108px;width:150px;height:160px;background:linear-gradient(160deg,#e4e4e4,#3a3a3a 70%,#262626)}
.bio{position:absolute;left:198px;top:110px;width:175px;font-size:7.2px;line-height:1.35;text-align:justify}
.bio p+p{margin-top:6px}
.locations{position:absolute;left:28px;top:280px;width:344px;height:108px;background:linear-gradient(180deg,#f2f2f2,#dedede);border-radius:10px;padding:10px 14px;font-size:7.4px;line-height:1.3}
.locations h3{color:var(--green);font-size:9px;font-weight:700;margin-bottom:6px}
.locations__cols{display:grid;grid-template-columns:1fr 1fr;gap:6px 18px}
.locations strong{display:block;font-weight:700;color:#333}
.collage{left:14px;top:92px;width:386px;height:180px;background:linear-gradient(90deg,#c9c9c9 0%,#9a9a9a 28%,#3c5f8f 45%,#d9b7a3 62%,#8c8c8c 80%,#c4c4c4)}
.accent-line{position:absolute;left:0;top:276px;width:400px;height:20px}
.doctor{position:absolute;left:20px;top:290px;width:362px;text-align:right}
.doctor h1{color:var(--green);font-size:22px;font-weight:900}
.doctor p{font-size:10px;line-height:1.35;color:#444}
.services{position:absolute;z-index:2;left:18px;top:364px;width:364px;height:60px;border-radius:12px;background:linear-gradient(180deg,#f4f4f4,#d9d9d9);box-shadow:0 3px 6px rgba(0,0,0,.2);display:grid;grid-template-columns:repeat(3,auto);gap:8px 14px;padding:10px 14px;font-size:9.5px;font-weight:700;color:#333;align-content:center}
.services li{list-style:none;display:flex;align-items:center;gap:5px}
.tick{width:10px;height:10px;flex:none}
.contact{position:absolute;z-index:2;left:0;width:400px;bottom:18px;text-align:center;color:#fff}
.contact__note{font-size:9px}
.contact__phone{font-size:16px;font-weight:900;margin-top:3px}
.contact__web{font-size:13px;font-weight:700}
.topic{position:absolute;left:34px;width:340px}
.topic h2{color:var(--green);font-size:11.5px;font-weight:900;letter-spacing:.3px;margin-bottom:8px}
.topic__body{display:flex;gap:12px}
.icon{width:58px;height:58px;border-radius:50%;flex:none;background:radial-gradient(circle at 40% 35%,#bdbdbd,#6e6e6e);box-shadow:0 3px 5px rgba(0,0,0,.3)}
.topic__text{font-size:7.2px;line-height:1.35;text-align:justify}
.topic__text p+p{margin-top:5px}
.link{color:var(--green)}
.fold{position:absolute;left:399px;top:0;width:2px;height:540px;background:rgba(0,0,0,.08);z-index:3}
</style>
</head>
<body>

<section class="spread spread--outside">
  <article class="page page--left">
    <div class="placeholder books" role="img" aria-label="Row of the surgeon's textbook covers"></div>
    <div class="books-fade"></div>
    <div class="placeholder portrait" role="img" aria-label="Portrait photo of the surgeon in a dark suit"></div>
    <div class="bio">
      <p>Dr. Hartwell is a nationally-recognized Upper Extremity Surgeon who has edited 7 textbooks, published over 45 original research papers and written 23 textbook chapters.</p>
      <p>Dr. Hartwell graduated Cum Laude from Eastbrook University and with honors from Lakemont Medical School. He completed his residency in Orthopaedic Surgery at Westvale University. In order to obtain expertise covering the entire upper extremity, he completed two fellowships, one in Hand Surgery and the other in Sports Medicine. He is board certified in Orthopaedic Surgery and has a Certificate of Additional Qualification in Hand Surgery.</p>
    </div>
    <div class="locations">
      <h3>Dr. Hartwell sees patients at the following locations:</h3>
      <div class="locations__cols">
        <div><strong>Central Medical Campus</strong>1200 Alder Street<br>Suite 410<br>Houston, Texas 77030</div>
        <div><strong>Riverside</strong>4820 Willow Bend Dr<br>Suite 115<br>Riverside, Texas 77500</div>
        <div><strong>Westlake</strong>318 Cedar Hollow Dr<br>Westlake, Texas 77400</div>
        <div><strong>Northgate</strong>9060 Brookfield Road West<br>Houston, Texas 77060</div>
      </div>
    </div>
    <svg class="band" viewBox="0 0 400 140" aria-hidden="true">
      <path d="M0 30 Q200 -8 400 40 L400 52 Q200 8 0 44Z" fill="#dcdcdc"/>
      <path d="M0 44 Q200 8 400 52 L400 140 L0 140Z" fill="var(--green)"/>
    </svg>
    <div class="brand" style="left:110px;top:394px"><span class="brand__dot"></span><span><span class="brand__name">NORTHRIDGE</span><span class="brand__sub">Orthopedic Group, L.L.P.</span></span></div>
    <div class="web" style="left:105px;bottom:20px">www.LimbForwardClinic.com</div>
  </article>

  <article class="page page--right">
    <div class="brand" style="right:28px;top:40px"><span class="brand__dot"></span><span><span class="brand__name">NORTHRIDGE</span><span class="brand__sub">Orthopedic Group, L.L.P.</span></span></div>
    <div class="placeholder collage" role="img" aria-label="Photo collage of patients holding painful elbows and wrists"></div>
    <svg class="accent-line" viewBox="0 0 400 20" aria-hidden="true"><path d="M0 4 Q200 18 400 6" stroke="var(--accent)" stroke-width="1.2" fill="none"/></svg>
    <div class="doctor">
      <h1>Daniel R. Hartwell, MD</h1>
      <p>Specialist in Surgery of the Hand, Wrist, Elbow &amp; Shoulder<br>Board Certified Orthopedic Surgeon<br>Certificate of Additional Qualification, Hand Surgery</p>
    </div>
    <ul class="services">
      <li><svg class="tick" viewBox="0 0 10 10"><circle cx="5" cy="5" r="4.3" fill="none" stroke="var(--green)"/><path d="M3 5.2l1.4 1.4L7.2 3.6" stroke="var(--green)" fill="none"/></svg>Carpal tunnel</li>
      <li><svg class="tick" viewBox="0 0 10 10"><circle cx="5" cy="5" r="4.3" fill="none" stroke="var(--green)"/><path d="M3 5.2l1.4 1.4L7.2 3.6" stroke="var(--green)" fill="none"/></svg>Cubital Tunnel</li>
      <li><svg class="tick" viewBox="0 0 10 10"><circle cx="5" cy="5" r="4.3" fill="none" stroke="var(--green)"/><path d="M3 5.2l1.4 1.4L7.2 3.6" stroke="var(--green)" fill="none"/></svg>Trigger Finger</li>
      <li><svg class="tick" viewBox="0 0 10 10"><circle cx="5" cy="5" r="4.3" fill="none" stroke="var(--green)"/><path d="M3 5.2l1.4 1.4L7.2 3.6" stroke="var(--green)" fill="none"/></svg>DeQuervain's tendinitis</li>
      <li style="grid-column:span 2"><svg class="tick" viewBox="0 0 10 10"><circle cx="5" cy="5" r="4.3" fill="none" stroke="var(--green)"/><path d="M3 5.2l1.4 1.4L7.2 3.6" stroke="var(--green)" fill="none"/></svg>Elbow &amp; Shoulder Pain</li>
    </ul>
    <svg class="band" viewBox="0 0 400 140" aria-hidden="true">
      <path d="M0 40 Q200 10 400 28 L400 40 Q200 22 0 52Z" fill="#dcdcdc"/>
      <path d="M0 52 Q200 22 400 40 L400 140 L0 140Z" fill="var(--green)"/>
    </svg>
    <div class="contact">
      <div class="contact__note">Appointments can be made online through BookACare.com</div>
      <div class="contact__phone">555-010-LIMB</div>
      <div class="contact__web">www.LimbForwardClinic.com</div>
    </div>
  </article>
  <div class="fold"></div>
</section>

<section class="spread spread--inside">
  <article class="page page--left">
    <div class="topic" style="top:28px">
      <h2>CARPAL TUNNEL SYNDROME</h2>
      <div class="topic__body">
        <div class="icon" role="img" aria-label="Icon of a hand with tingling fingers"></div>
        <div class="topic__text">
          <p>Carpal Tunnel Syndrome occurs when the main nerve to the hand gets pinched at the wrist. This leads to fingers feeling numb, asleep or cold, or having pins and needles in them. Symptoms are usually worse at night or upon awakening. If you wake up at night and have to shake your hand out to get relief, you probably have carpal tunnel syndrome. Symptoms also often occur with gripping, such as when driving, writing or holding books, phones or tools.</p>
          <p>Unless the syndrome has led to nerve damage, initial treatment often involves splinting the wrist at night. If that doesn't work, the tunnel can be released. The least invasive technique is the single incision endoscopic release, a quick outpatient procedure with a small incision. There is less pain and a quicker return to work and other activities. To see a video of an Endoscopic Carpal Tunnel Release please go to: <span class="link">www.LimbForwardClinic.com</span></p>
        </div>
      </div>
    </div>
    <div class="topic" style="top:238px">
      <h2>CUBITAL TUNNEL SYNDROME</h2>
      <div class="topic__body">
        <div class="icon" role="img" aria-label="Icon of hand and wrist bones"></div>
        <div class="topic__text">
          <p>Cubital tunnel syndrome occurs when the funny bone nerve gets pinched at the elbow. This leads to tingling and numbness of the small finger, usually at night or when talking on the phone. Numbness may also occur when the elbow rests on a hard surface.</p>
          <p>Unless nerve damage has occurred, treatment starts with avoiding pressure on the elbow and not resting it on desks or arm rests. Use a hands-free device to avoid holding phones for long periods.</p>
          <p>If this fails, the least invasive definitive treatment is an Endoscopic Cubital Tunnel Release. This outpatient procedure allows an early return to activities with a low complication rate. To see a video please go to: <span class="link">www.LimbForwardClinic.com</span></p>
        </div>
      </div>
    </div>
    <svg class="band" viewBox="0 0 400 140" aria-hidden="true">
      <path d="M0 30 Q200 -8 400 40 L400 52 Q200 8 0 44Z" fill="#dcdcdc"/>
      <path d="M0 44 Q200 8 400 52 L400 140 L0 140Z" fill="var(--green)"/>
    </svg>
    <div class="brand brand--light" style="left:40px;top:455px"><span class="brand__dot"></span><span><span class="brand__name">NORTHRIDGE</span><span class="brand__sub">Orthopedic Group, L.L.P.</span></span></div>
  </article>

  <article class="page page--right">
    <div class="topic" style="top:60px;left:30px">
      <h2>TRIGGER FINGER</h2>
      <div class="topic__body">
        <div class="icon" role="img" aria-label="Icon of a finger pressing down"></div>
        <div class="topic__text">
          <p>Trigger finger occurs when the tendon that moves the finger gets pinched in its tunnel. This causes the finger to catch or lock, which is often worse in the morning. The catching can be quite painful, and the finger may be stuck straight or difficult to bend.</p>
          <p>Splinting may temporarily prevent the catching but does not treat the problem. If caught early, a steroid injection can be curative. After several months the chance of success is lower.</p>
          <p>If triggering returns after injection, the problem can be treated with a minimally-invasive release. To see a video please go to: <span class="link">www.LimbForwardClinic.com</span></p>
        </div>
      </div>
    </div>
    <div class="topic" style="top:248px;left:30px">
      <h2>WRIST PAIN</h2>
      <div class="topic__body">
        <div class="icon" role="img" aria-label="Icon of two hands held together"></div>
        <div class="topic__text">
          <p>Wrist pain may have many causes and diagnosis is best made by a fellowship-trained Hand Surgeon. The most common cause is DeQuervain's tendinitis, which causes pain on the thumb side of the wrist when tendons get pinched in their tunnel.</p>
          <p>It is common in mothers who repetitively lift small children, and in people lifting heavy bags. Initial treatment is to lift with the palm up and keep the thumb relaxed. A single steroid injection is often very effective if treated early.</p>
          <p>If the tendinitis recurs, an outpatient tendon release is very effective. To see a video please go to: <span class="link">www.LimbForwardClinic.com</span></p>
        </div>
      </div>
    </div>
    <svg class="band" viewBox="0 0 400 140" aria-hidden="true">
      <path d="M0 40 Q200 10 400 28 L400 40 Q200 22 0 52Z" fill="#dcdcdc"/>
      <path d="M0 52 Q200 22 400 40 L400 140 L0 140Z" fill="var(--green)"/>
    </svg>
    <div class="web" style="left:90px;bottom:24px">www.LimbForwardClinic.com</div>
  </article>
  <div class="fold"></div>
</section>

</body>
</html>
```